Ladies Of Tumbling - Climbing to the Summit poster

Apparatus Sport Coastal needs a poster to promote the "Ladies Of Tumbling - Climbing to the Summit" program. The program is a developmental and leadership program for females with a focus on senior management and governance.

There a a number of different ways women can be involved in the program:
- professional development workshop series
- good governance program
- coaching courses
- alumni network

The three key words of the program are LEAD, INFLUENCE and CHANGE

Women have to apply for the workshop series and governance program.

Including gymnastic specific images in the design is NOT essential, the poster should have an inspirational feel, encouraging women to further their professional expertise and cultivate a long term career in the sport.

The poster will be sent out to clubs to put on their noticeboards so should stand out.

The Ladies Of Tumbling logo uses the following PMS colours - 2758, 3005, 220, 2603, 327, 485, 158, 1235. These PMS colours are the gymsport colours and should be used in preference to others.

Target Market(s)

Both younger women aspiring for a career in gymnastics and established gymnastic sport professionals

Industry/Entity Type

Leadership

Requirements
Must have
• The poster needs to include some text which is below - however depending on design the text can be adjusted.

"Ladies Of Tumbling—Climbing to the Summit is a comprehensive developmental and leadership program for females enabling them to LEAD, INFLUENCE and CHANGE.

For ways to be involved in this free program got to www.apparatussportcoastal.org.au"

The only call to action is website address so it should be prominent.
www.apparatussportcoastal.org.au

Must include Apparatus Sport Coastal and State Government logos, which can be discreet.
Nice to have
• Design to work and print in both A3 and A4 size. A3 will be the predominant size.
Modern fonts
Should not have
• Traditional gymnastic images or graphics

```html
<!DOCTYPE html>
<html lang="en">
<head>
<meta charset="utf-8">
<title>Ladies Of Tumbling - Climbing to the Summit</title>
<link rel="stylesheet" href="https://fonts.googleapis.com/css2?family=Arimo:wght@400;700&display=swap">
<style>
  :root {
    --paper: #f6b673;
    --teal: #1f8d80;
    --blue: #3e6bb7;
    --mauve: #a8606c;
    --rose: #c9717b;
    --plum: #8c5565;
    --navy: #1f3766;
    --slate: #3f4e66;
    --ribbon-a: #8fc8e6;
    --ribbon-b: #d77aa6;
    --ribbon-c: #f4c9a2;
  }
  * { margin: 0; padding: 0; box-sizing: border-box; }
  html, body { width: 848px; height: 1200px; overflow: hidden; }
  body { background: var(--paper); font-family: "Arimo", Arial, sans-serif; }
  .poster { position: relative; width: 848px; height: 1200px; background: var(--paper); overflow: hidden; }

  .hero-figure {
    position: absolute; left: 290px; top: 12px; width: 230px; height: 520px;
    background:
      radial-gradient(ellipse 45% 18% at 50% 86%, rgba(215,122,166,.75), rgba(143,200,230,.45) 60%, transparent 100%),
      linear-gradient(180deg, transparent 0%, rgba(244,201,162,.5) 45%, rgba(143,200,230,.35) 80%, transparent 100%);
    border-radius: 40% 40% 45% 45%;
  }

  .title-block { position: absolute; top: 545px; left: 0; width: 100%; text-align: center; }
  .program-name { font-size: 40px; font-weight: 700; color: var(--teal); letter-spacing: 1.5px; line-height: 1.1; }
  .program-tagline { margin-top: 10px; font-size: 26px; font-weight: 700; color: var(--blue); letter-spacing: .5px; }

  .pillars { position: absolute; top: 736px; left: 0; width: 100%; text-align: center;
    font-size: 25px; font-weight: 700; color: var(--mauve); letter-spacing: 1px;
    text-shadow: 1px 1px 0 rgba(80,40,50,.45); }
  .pathways { position: absolute; top: 786px; left: 0; width: 100%; list-style: none; text-align: center;
    font-size: 25px; font-weight: 700; color: var(--rose); letter-spacing: 1px; line-height: 34px; }

  .website { position: absolute; top: 1046px; left: 0; width: 100%; text-align: center;
    font-size: 23px; font-weight: 700; color: var(--plum); letter-spacing: 1px;
    text-shadow: 1px 1px 0 rgba(60,30,40,.4); }

  .partner { position: absolute; display: flex; align-items: center; gap: 12px; }
  .partner-government { left: 24px; top: 1110px; }
  .partner-government .mark { width: 62px; height: 62px; background: var(--slate); }
  .partner-government .name { font-size: 15px; font-weight: 400; color: var(--slate); line-height: 1.25; width: 210px; }
  .partner-host { right: 20px; top: 1108px; }
  .partner-host .mark { width: 68px; height: 68px; border-radius: 50%; background: var(--navy); }
  .partner-host .name { font-size: 22px; font-weight: 400; color: var(--navy); line-height: 1.15; width: 160px; }
</style>
</head>
<body>
<main class="poster">
  <div class="hero-figure" role="img" aria-label="Flowing ribbon illustration of a rising female figure with a colourful burst at its base"></div>

  <header class="title-block">
    <h1 class="program-name">LADIES OF TUMBLING</h1>
    <p class="program-tagline">Climbing to the summit</p>
  </header>

  <p class="pillars">LEAD, INFLUENCE and CHANGE</p>
  <ul class="pathways">
    <li>- professional development workshop series</li>
    <li>- good governance program</li>
    <li>- coaching courses</li>
    <li>- alumni network</li>
  </ul>

  <p class="website">www.apparatussportcoastal.org.au</p>

  <footer>
    <div class="partner partner-government">
      <span class="mark"></span>
      <span class="name">Coastal State Office of Community Planning</span>
    </div>
    <div class="partner partner-host">
      <span class="mark"></span>
      <span class="name">Apparatus Sport Coastal</span>
    </div>
  </footer>
</main>
</body>
</html>
```